PEACFUL ACUPUNCTURE PRACTITIONER NEEDS A NEW COAT

I need a new design for an exiting website http://stillwillowneedlework.example/ for a acupuncturist. This will be a minimalism design with lots and lots of white space. Home page and one interior page. Please keep the feeling of calm and peaceful serenity. For Color scheme: https://www.harborfernclinic.example/fertility. The bottom part of the home page with sections and links to the service pages: https://mossgatewellness.example/. The client likes this the best: http://qlhealing.example/. I'm attaching the logo and content pages.

Target Market(s)

Women

Industry/Entity Type

Wellness, health, wellbeing, meditation

Number of Pages Required

2 page

Font styles to use
Sans Serif
Decorative

Colors

Designer to choose colors to be used in the design.

Requirements
Must have
Nice to have
• Follow new website drafts and links
Should not have
• Busy with bright colors. No poping

```html
<!DOCTYPE html>
<html lang="en">
<head>
<meta charset="utf-8">
<title>Still Willow Acupuncture</title>
<link rel="stylesheet" href="https://fonts.googleapis.com/css2?family=Mulish:wght@400;500;600&display=swap">
<style>
:root{
  --backdrop:#dde6e4;
  --page:#ffffff;
  --cream:#fcf9f5;
  --card-edge:#f3efe9;
  --heading:#a9b4c4;
  --rose:#c4929c;
  --ink:#222222;
  --nav:#5b5b5b;
  --headline:#555050;
  --rule:#e6e6e6;
  --button:#aebacb;
  --logo:#6f6a6b;
}
*{box-sizing:border-box;margin:0;padding:0}
html,body{width:1200px;height:2230px;overflow:hidden}
body{background:var(--backdrop);font-family:'Mulish',sans-serif;color:var(--ink)}
.page{position:absolute;left:142px;top:0;width:922px;height:2230px;background:var(--page)}
.site-header{height:95px;display:flex;align-items:center;justify-content:center}
.brand{display:flex;align-items:center;gap:12px}
.brand-mark{width:52px;height:52px;border-radius:50%;border:2px solid var(--rose)}
.brand-name{font-size:30px;font-weight:400;color:var(--logo);letter-spacing:.5px}
.main-nav{height:36px;border-top:1px solid var(--rule);border-bottom:1px solid var(--rule);display:flex;justify-content:space-between;align-items:center;padding:0 6px 0 11px}
.main-nav a,.footer-nav a{font-size:12.5px;color:var(--nav);text-decoration:none}
.hero{position:absolute;top:140px;left:0;width:922px;height:524px;
  background:linear-gradient(180deg,#efe2cf 0%,#f3d9a8 35%,#e9c58c 55%,#b8a48c 75%,#8f8478 100%)}
.hero-title{position:absolute;left:25px;top:168px;width:440px;font-size:31px;font-weight:500;line-height:45px;color:var(--headline)}
.philosophy{position:absolute;top:664px;left:0;width:922px;height:358px;text-align:center;padding:68px 36px 0}
.section-title{font-size:36px;font-weight:500;color:var(--heading)}
.philosophy p{font-size:15px;line-height:28px;margin-top:6px}
.philosophy p+p{margin-top:0}
.focus{position:absolute;top:1022px;left:0;width:922px;height:528px;background:var(--cream);text-align:center;padding-top:70px}
.cards{display:flex;gap:14px;margin:18px 8px 0}
.card{width:214px;height:315px;border:3px solid var(--card-edge);background:var(--cream);padding-top:26px}
.card-photo{width:111px;height:111px;border-radius:50%;margin:0 auto}
.card h3{font-size:15.5px;font-weight:500;color:var(--rose);margin-top:21px}
.card p{font-size:13px;line-height:23px;margin-top:9px;padding:0 8px}
.card-arrow{display:block;margin:14px auto 0}
.help{position:absolute;top:1550px;left:0;width:922px;height:308px;text-align:center;padding-top:74px}
.help p{font-size:15px;line-height:28px;margin:6px 50px 0}
.call-button{display:inline-flex;align-items:center;gap:12px;margin-top:10px;height:43px;padding:0 15px;background:var(--button);border-radius:3px;font-size:15.5px;color:var(--ink)}
.site-footer{position:absolute;top:1858px;left:0;width:922px;height:372px;background:var(--cream)}
.footer-brand{height:140px;display:flex;align-items:flex-end;justify-content:center;padding-bottom:2px}
.footer-nav{display:flex;justify-content:space-between;align-items:center;height:55px;margin-top:16px;padding:0 16px 0 9px;border-bottom:1px solid var(--rule)}
.contact-row{display:flex;height:100px;align-items:center;padding:0 16px;border-bottom:1px solid var(--rule)}
.contact{display:flex;align-items:center;gap:14px;font-size:13px;line-height:19px;color:#444}
.contact-icon{width:45px;height:45px;border-radius:50%;border:1px solid #d8d8d8;display:flex;align-items:center;justify-content:center;background:#fff}
.copyright{text-align:center;font-size:12.5px;padding-top:14px;color:#333}
</style>
</head>
<body>
<div class="page">
  <header class="site-header">
    <div class="brand"><span class="brand-mark"></span><span class="brand-name">Still Willow Acupuncture</span></div>
  </header>
  <nav class="main-nav">
    <a href="#">Home</a><a href="#">About</a><a href="#">Fertility &amp; Pregnancy</a><a href="#">Hormone Balance</a><a href="#">Strength &amp; Structure</a><a href="#">Emotional Wellbeing</a><a href="#">Online Shop</a><a href="#">Testimonials</a><a href="#">Contact</a>
  </nav>

  <section class="hero" role="img" aria-label="Photo of a woman in a white dress with open arms on a beach at golden sunset">
    <h1 class="hero-title">Our Goal Is To Help Every Woman Develop A Deeper Sense of Communication With Her Body.</h1>
  </section>

  <section class="philosophy">
    <h2 class="section-title">Philosophy of Care</h2>
    <p>Acupuncture &amp; Chinese Herbal Medicine are rooted in over 3000 years of history and tradition. As a complete medical system that has remained flexible and relevant we honor what has worked from the past while embracing the medicine of tomorrow.</p>
    <p>At Still Willow Acupuncture we provide compassionate, respectful and empowering care in a safe and inclusive environment. Our goal is to harmonize physical, mental and emotional wellbeing to strengthen the Still Willow from which we all strive to live.</p>
  </section>

  <section class="focus">
    <h2 class="section-title">Areas of Focus</h2>
    <div class="cards">
      <article class="card">
        <div class="card-photo" role="img" aria-label="Photo of a bird nest among green leaves" style="background:radial-gradient(circle,#2e2a22 25%,#6b5a3e 50%,#5f9a3c 80%)"></div>
        <h3>Fertility &amp; Pregnancy</h3>
        <p>Lorem ipsum dolor sidfat amet, consectetuer adipiscing elit, sed diam nonummy nibh.</p>
        <svg class="card-arrow" width="16" height="8" viewBox="0 0 16 8"><path d="M0 4H14M10 1l4 3-4 3" stroke="#c4929c" stroke-width="1.6" fill="none"/></svg>
      </article>
      <article class="card">
        <div class="card-photo" role="img" aria-label="Photo of balanced stones on a seaside rock" style="background:linear-gradient(180deg,#3f86d0 0%,#8fc2ea 50%,#d8754a 62%,#3f74a8 80%)"></div>
        <h3>Emotional&nbsp; Wellbeing</h3>
        <p>Lorem ipsum dolor sidfat amet, consectetuer adipiscing elit, sed diam nonummy nibh.</p>
        <svg class="card-arrow" width="16" height="8" viewBox="0 0 16 8"><path d="M0 4H14M10 1l4 3-4 3" stroke="#c4929c" stroke-width="1.6" fill="none"/></svg>
      </article>
      <article class="card">
        <div class="card-photo" role="img" aria-label="Photo of a stack of pebbles balanced on a large stone" style="background:radial-gradient(circle at 55% 55%,#c9bfb3 0%,#8c857d 35%,#6e9ed2 60%,#3f7bbf 100%)"></div>
        <h3>Hormone Balance</h3>
        <p>Lorem ipsum dolor sidfat amet, consectetuer adipiscing elit, sed diam nonummy nibh.</p>
        <svg class="card-arrow" width="16" height="8" viewBox="0 0 16 8"><path d="M0 4H14M10 1l4 3-4 3" stroke="#c4929c" stroke-width="1.6" fill="none"/></svg>
      </article>
      <article class="card">
        <div class="card-photo" role="img" aria-label="Photo of a single tree in a green field" style="background:linear-gradient(180deg,#e6eef5 0%,#2f4a26 35%,#31522a 75%,#6f9a45 100%)"></div>
        <h3>Strength &amp; Structure</h3>
        <p>Lorem ipsum dolor sidfat amet, consectetuer adipiscing elit, sed diam nonummy nibh.</p>
        <svg class="card-arrow" width="16" height="8" viewBox="0 0 16 8"><path d="M0 4H14M10 1l4 3-4 3" stroke="#c4929c" stroke-width="1.6" fill="none"/></svg>
      </article>
    </div>
  </section>

  <section class="help">
    <h2 class="section-title">Acupuncture Can Help!</h2>
    <p>Schedule A Free 30 Minute ConsultationConsultations are always available to help answer any questions you may have about acupuncture or herbal medicine in a relaxed environment.</p>
    <span class="call-button">
      <svg width="22" height="22" viewBox="0 0 24 24" fill="none" stroke="#333" stroke-width="1.3"><path d="M5 3l4 4-2 3c1 3 4 6 7 7l3-2 4 4-3 3C10 21 3 14 2 6z"/><path d="M14 3a7 7 0 0 1 7 7M14 6a4 4 0 0 1 4 4"/></svg>
      Call Us: 555-014-3220
    </span>
  </section>

  <footer class="site-footer">
    <div class="footer-brand"><div class="brand"><span class="brand-mark"></span><span class="brand-name">Still Willow Acupuncture</span></div></div>
    <nav class="footer-nav">
      <a href="#">Home</a><a href="#">About</a><a href="#">Fertility &amp; Pregnancy</a><a href="#">Hormone Balance</a><a href="#">Strength &amp; Structure</a><a href="#">Emotional Wellbeing</a><a href="#">Online Shop</a><a href="#">Testimonials</a><a href="#">Contact</a>
    </nav>
    <div class="contact-row">
      <div class="contact" style="width:372px">
        <span class="contact-icon"><svg width="18" height="20" viewBox="0 0 18 22" fill="none" stroke="#666" stroke-width="1.2"><path d="M9 21s7-7 7-12A7 7 0 0 0 2 9c0 5 7 12 7 12z"/><circle cx="9" cy="9" r="2.5"/></svg></span>
        <span>Still Willow Acupuncture<br>18 Alder Row | Easthollow MA</span>
      </div>
      <div class="contact" style="width:245px">
        <span class="contact-icon"><svg width="20" height="20" viewBox="0 0 24 24" fill="none" stroke="#666" stroke-width="1.2"><path d="M5 3l4 4-2 3c1 3 4 6 7 7l3-2 4 4-3 3C10 21 3 14 2 6z"/><path d="M14 3a7 7 0 0 1 7 7M14 6a4 4 0 0 1 4 4"/></svg></span>
        <span>Call Us<br>555-014-3220</span>
      </div>
      <div class="contact">
        <span class="contact-icon"><svg width="20" height="18" viewBox="0 0 22 20" fill="none" stroke="#666" stroke-width="1.2"><path d="M2 8l9-6 9 6v10H2z"/><path d="M2 8l9 6 9-6"/></svg></span>
        <span>Email Us<br>mara@stillwillowneedlework.example</span>
      </div>
    </div>
    <p class="copyright">Copyright © 2021 Still Willow Acupuncture. All Rights Reserved.</p>
  </footer>
</div>
</body>
</html>
```